Creative/innovative law firm website

A law firm website that immediately looks different from other law firm websites. We like the color scheme (dark background with warm, neutral colors) and simple, organic logos (trees, leaves, etc.) of this website: https://brambleworth.legal/

We'll be offering creative/innovative solutions to complex problems faced by state governments, industries, other law firms, and individuals. We're located in Montana (U.S.A.), and the outdoors is a huge part of our lives and identities.

We will need a home page, an "About Us" page with a separate subpage for each attorney (two attorneys), a blog or "Publications" page, a payment portal (which will integrate with Quillo), and a "Services" page.

```html
<!DOCTYPE html>
<html lang="en">
<head>
<meta charset="utf-8">
<title>Law Firm — Home</title>
<link href="https://fonts.googleapis.com/css2?family=Libre+Bodoni:wght@700&family=Nunito+Sans:wght@400;600;700;800&display=swap" rel="stylesheet">
<style>
:root{
  --gold-light:#fcd872;
  --gold:#f2a93a;
  --gold-deep:#ee9a25;
  --panel:#1f1f21;
  --panel-alt:#1a1a1a;
  --card:#3a3a3b;
  --field:#3d3d3e;
  --text:#ffffff;
  --muted:#d4d4d4;
  --hero-text:#4a4a4a;
  --gold-grad:linear-gradient(90deg,var(--gold-light),var(--gold-deep));
}
*{box-sizing:border-box;margin:0;padding:0}
html,body{width:1200px;height:3309px;overflow:hidden}
body{font-family:"Nunito Sans",Arial,sans-serif;color:var(--text);background:var(--panel);position:relative}
.serif{font-family:"Libre Bodoni",Georgia,serif;font-weight:700}
.abs{position:absolute}
.btn{position:absolute;display:flex;align-items:center;justify-content:center;background:var(--gold-grad);color:#1d1d1d;font-weight:800;font-size:14px;border-radius:30px;letter-spacing:.3px;box-shadow:0 4px 10px rgba(0,0,0,.18)}

/* hero */
.hero{position:absolute;left:0;top:0;width:1200px;height:591px;overflow:hidden}
.hero-photo{position:absolute;inset:0;background:linear-gradient(90deg,#f4f5f6 0%,#eceeef 40%,#d8d6d2 62%,#c9b48c 78%,#8a7b6a 100%)}
.logo{position:absolute;display:flex;align-items:center;gap:14px;font-weight:700;letter-spacing:2px}
.logo .mark{border-radius:50%;border:3px solid var(--gold)}
.nav{position:absolute;top:42px;left:512px;display:flex;gap:36px;font-size:14px;color:#333}
.nav a{color:inherit;text-decoration:none}
.nav .active{color:var(--gold);border-bottom:2px solid var(--gold);padding-bottom:6px}
.hero h1{position:absolute;left:113px;top:230px;font-size:62px;line-height:62px;color:#222;letter-spacing:1px}
.hero p{position:absolute;left:113px;top:296px;width:440px;font-size:17px;line-height:26px;color:var(--hero-text);font-weight:600}
.arrow{position:absolute;width:60px;height:60px;border-radius:50%;border:1.5px solid rgba(255,255,255,.95);display:flex;align-items:center;justify-content:center;box-shadow:0 0 6px rgba(0,0,0,.12)}

/* about */
.about{position:absolute;left:0;top:591px;width:1200px;height:491px;background:var(--panel)}
h2{font-family:"Libre Bodoni",Georgia,serif;font-weight:700;font-size:36px;letter-spacing:2px;color:#fff}
.center{text-align:center;position:absolute;left:0;width:1200px}

/* services */
.services{position:absolute;left:0;top:1082px;width:1200px;height:501px;background:var(--panel-alt)}
.svc{position:absolute;top:168px;width:231px;height:248px;background:var(--card);border-radius:8px;display:flex;flex-direction:column;align-items:center}
.svc svg{margin-top:30px}
.svc .label{font-family:"Libre Bodoni",Georgia,serif;font-weight:700;color:var(--gold);font-size:23px;letter-spacing:1.5px;text-align:center;line-height:33px;position:absolute;top:156px;height:66px;display:flex;align-items:center;width:100%;justify-content:center}

/* blog */
.blog{position:absolute;left:0;top:1583px;width:1200px;height:730px;background:var(--panel)}
.post{position:absolute;top:158px;width:469px;height:402px;background:var(--card);border-radius:8px}
.post .thumb{position:absolute;left:10px;top:9px;width:450px;height:186px;border-radius:8px;border:2px solid #fff}
.post h3{position:absolute;top:212px;left:20px;right:20px;text-align:center;font-family:"Libre Bodoni",Georgia,serif;font-weight:700;font-size:22px;line-height:28px;color:#efefef}
.post p{position:absolute;top:278px;left:18px;right:18px;text-align:center;font-size:13px;line-height:21.5px;color:var(--muted)}
.post .more{position:absolute;top:371px;left:0;width:100%;text-align:center;color:var(--gold);font-weight:800;font-size:14px;line-height:18px;text-decoration:underline}

/* contact */
.contact{position:absolute;left:0;top:2313px;width:1200px;height:585px;background:var(--panel-alt)}
.field{position:absolute;background:var(--field);display:flex;align-items:center;gap:12px;padding-left:14px;font-size:12px;color:#cfcfcf;letter-spacing:.4px}

/* footer */
.footer{position:absolute;left:0;top:2898px;width:1200px;height:411px;background:var(--panel)}
.col{position:absolute;top:106px}
.col h4{font-family:"Libre Bodoni",Georgia,serif;font-weight:700;font-size:19px;letter-spacing:1px;white-space:nowrap}
.col .bar{width:46px;height:3px;background:var(--gold);margin:12px 0 14px}
.col li{list-style:none;font-size:12.5px;font-weight:600;line-height:24px;letter-spacing:.3px;white-space:nowrap}
.social{position:absolute;top:231px;width:44px;height:44px;border-radius:50%;background:var(--gold-grad)}
</style>
</head>
<body>

<header class="hero">
  <div class="hero-photo" role="img" aria-label="Bright office scene with three colleagues reviewing documents at a laptop beside a potted plant"></div>
  <div class="logo" style="left:118px;top:26px;font-size:20px;color:#333">
    <span class="mark" style="width:62px;height:62px"></span>LAW FIRM
  </div>
  <nav class="nav">
    <a class="active">HOME</a><a>ABOUT US</a><a>SERVICES</a><a>PUBLICATIONS</a>
  </nav>
  <div class="btn" style="left:936px;top:29px;width:152px;height:44px;font-size:13px">CONTACT US</div>
  <div class="arrow" style="left:23px;top:266px">
    <svg width="22" height="14" viewBox="0 0 22 14"><path d="M21 7H2M8 1 2 7l6 6" stroke="#fff" stroke-width="2" fill="none"/></svg>
  </div>
  <div class="arrow" style="left:1116px;top:266px">
    <svg width="22" height="14" viewBox="0 0 22 14"><path d="M1 7h19M14 1l6 6-6 6" stroke="#fff" stroke-width="2" fill="none"/></svg>
  </div>
  <h1 class="serif">LAW FIRM</h1>
  <p>Perspiciatis unde omnis istenatus errorsit voluptatem accusantium doloremque.</p>
  <div class="btn" style="left:113px;top:366px;width:208px;height:43px;font-size:13px">BOOK AN APPOINTMENT</div>
</header>

<section class="about">
  <div class="abs" style="left:98px;top:93px;width:438px;height:332px;background:var(--gold);border-radius:6px"></div>
  <div class="abs" role="img" aria-label="Photo of a couple meeting with an advisor across a desk" style="left:112px;top:80px;width:438px;height:333px;border-radius:6px;background:linear-gradient(100deg,#6b4a32 0%,#8b6a55 30%,#cfc9c4 60%,#efeeec 100%)"></div>
  <h2 class="abs" style="left:600px;top:96px">ABOUT US</h2>
  <p class="abs" style="left:600px;top:152px;width:440px;font-size:15px;line-height:26px;color:#e6e6e6">Perspiciatis unde omnis iste natus error sit voluptatem accusantium doloremque laudantium, totam rem aperiam, eaque ipsa quaeab illo inventore veritatis et quasi architecto beatae vitae dicta sunt explicabo. Nemo enim ipsam voluptatem quia voluptassit aspernaturaut</p>
  <div class="btn" style="left:600px;top:302px;width:132px;height:45px">LEARN MORE</div>
</section>

<section class="services">
  <h2 class="center" style="top:78px">OUR SERVICES</h2>
  <div class="svc" style="left:112px">
    <svg width="84" height="84" viewBox="0 0 84 84" fill="none" stroke="#fff" stroke-width="4" stroke-linejoin="round"><path d="M8 28 42 10l34 18z"/><path d="M14 36v36M30 36v36M54 36v36M70 36v36M6 78h72"/></svg>
    <div class="label">STATE<br>GOVERNMENTS</div>
  </div>
  <div class="svc" style="left:360px">
    <svg width="84" height="84" viewBox="0 0 84 84" fill="none" stroke="#fff" stroke-width="4" stroke-linejoin="round"><path d="M8 78V40l20 12V40l20 12V20h20v58z"/><path d="M4 78h76"/></svg>
    <div class="label">INDUSTRIES</div>
  </div>
  <div class="svc" style="left:609px">
    <svg width="84" height="84" viewBox="0 0 84 84" fill="none" stroke="#fff" stroke-width="4" stroke-linejoin="round"><path d="M42 10v64M14 22h56M28 76h28"/><path d="M22 22 10 48h24zM62 22 50 48h24z"/></svg>
    <div class="label">OTHER LAW<br>FIRMS</div>
  </div>
  <div class="svc" style="left:857px">
    <svg width="84" height="84" viewBox="0 0 84 84" fill="none" stroke="#fff" stroke-width="4"><circle cx="42" cy="28" r="14"/><path d="M14 76c0-16 12-26 28-26s28 10 28 26"/></svg>
    <div class="label">INDIVIDUALS</div>
  </div>
</section>

<section class="blog">
  <h2 class="center" style="top:82px">LATEST BLOG</h2>
  <article class="post" style="left:112px">
    <div class="thumb" role="img" aria-label="Photo of a lawyer consulting a client at an office desk" style="background:linear-gradient(100deg,#cfd6df 0%,#6f7784 40%,#2f4a78 70%,#e8ebef 100%)"></div>
    <h3>Accusamus etiusto odio dignissimos ducimus quiblanditiis</h3>
    <p>Perspiciatis unde omnis iste natus error sit voluptatem accusantium doloremque laudantium, totam rem aperiam, eaque ipsa quaeab illo inventore veritatis et quasi architecto beatae vitae dicta sunt explicabo. Nemo enim ipsam voluptatem quia voluptassit aspernaturaut</p>
    <div class="more">LEARN MORE</div>
  </article>
  <article class="post" style="left:619px">
    <div class="thumb" role="img" aria-label="Group photo of a smiling office team" style="background:linear-gradient(90deg,#c9a79c 0%,#dfe2e6 35%,#d6d9de 65%,#bfc4cc 100%)"></div>
    <h3>Accusamus etiusto odio dignissimos ducimus quiblanditiis</h3>
    <p>Perspiciatis unde omnis iste natus error sit voluptatem accusantium doloremque laudantium, totam rem aperiam, eaque ipsa quaeab illo inventore veritatis et quasi architecto beatae vitae dicta sunt explicabo. Nemo enim ipsam voluptatem quia voluptassit aspernaturaut</p>
    <div class="more">LEARN MORE</div>
  </article>
  <div class="btn" style="left:504px;top:596px;width:191px;height:44px">VIEW MORE</div>
</section>

<section class="contact">
  <h2 class="center" style="top:76px">REACH US</h2>
  <p class="center" style="top:126px;font-size:17px;line-height:26px;font-weight:800;padding:0 270px">Perspiciatis unde omnis istenatus errorsit voluptatem accusantium doloremque laudantium totam remaperiam</p>
  <div class="field" style="left:234px;top:185px;width:357px;height:44px"><svg width="14" height="14" viewBox="0 0 14 14" fill="#aaa"><circle cx="7" cy="4" r="3.5"/><path d="M1 14a6 5 0 0 1 12 0z"/></svg>FIRST NAME</div>
  <div class="field" style="left:608px;top:185px;width:357px;height:44px"><svg width="14" height="14" viewBox="0 0 14 14" fill="#aaa"><circle cx="7" cy="4" r="3.5"/><path d="M1 14a6 5 0 0 1 12 0z"/></svg>LAST NAME</div>
  <div class="field" style="left:234px;top:247px;width:357px;height:45px"><svg width="16" height="12" viewBox="0 0 16 12" fill="none" stroke="#aaa" stroke-width="1.5"><rect x="1" y="1" width="14" height="10"/><path d="m1 1 7 6 7-6"/></svg>EMAIL</div>
  <div class="field" style="left:608px;top:247px;width:357px;height:45px"><svg width="14" height="14" viewBox="0 0 14 14" fill="#aaa"><path d="M3 1 5 4 4 6q1 3 4 4l2-1 3 2-2 2Q2 12 1 3z"/></svg>PHONE</div>
  <div class="field" style="left:234px;top:308px;width:731px;height:130px;align-items:flex-start;padding-top:14px"><svg width="14" height="14" viewBox="0 0 14 14" stroke="#aaa" stroke-width="1.5"><path d="M1 1l12 12"/></svg>MESSAGE</div>
  <div class="btn" style="left:504px;top:469px;width:191px;height:44px">SUBMIT</div>
</section>

<footer class="footer">
  <div class="logo" style="left:125px;top:114px;font-size:27px;color:#fff;letter-spacing:1.5px;gap:16px">
    <span class="mark" style="width:80px;height:80px"></span>LAW FIRM
  </div>
  <span class="social" style="left:195px" aria-label="Social link"></span>
  <span class="social" style="left:254px" aria-label="Social link"></span>
  <div class="col" style="left:452px"><h4>QUICK LINKS</h4><div class="bar"></div><ul><li>HOME</li><li>ABOUT US</li><li>SERVICES</li><li>PUBLICATIONS</li><li>CONTACT US</li></ul></div>
  <div class="col" style="left:637px"><h4>OUR POLICIES</h4><div class="bar"></div><ul><li>TERMS &amp; CONDITIONS</li><li>PRIVACY POLICY</li><li>COMPANY VALUES</li><li>CORPORATE ETHICS POLICY</li><li>ANTI SLAVERY POLICY</li></ul></div>
  <div class="col" style="left:880px"><h4>SUPPORT</h4><div class="bar"></div><ul><li>TEAM</li><li>ABOUT US</li><li>CAREERS</li><li>OUR VALUES</li></ul></div>
  <div class="col" style="left:1034px"><h4>LINKS</h4><div class="bar"></div><ul><li>COPYRIGHT</li><li>LEGAL</li><li>PRIVACY</li><li>ACCESSIBILITY</li><li>SITEMAP</li></ul></div>
  <div class="abs" style="left:112px;top:330px;width:976px;height:1px;background:#555"></div>
  <div class="abs" style="left:1124px;top:316px;width:44px;height:44px;border-radius:50%;background:var(--gold-deep);display:flex;align-items:center;justify-content:center">
    <svg width="14" height="9" viewBox="0 0 14 9"><path d="M1 8l6-6 6 6" stroke="#fff" stroke-width="2" fill="none"/></svg>
  </div>
  <p class="center" style="top:360px;font-size:14px;font-weight:800">©2021.All rights reserved.</p>
</footer>

</body>
</html>
```